Medical Clinic flyer with modern classy touch

Create a captivating design for a multispecialty group office that offers primary care, psychiatry, physical rehabilitation and services that extend beyond traditional medicine. Our group is geared towards helping an individual or the entire family from infancy to geriatric. Wherever the patient is at our physicians will be by there side.

Target Market(s)

We target all ages young and old.

Industry/Entity Type

Health Care

Font styles to use
Sans Serif

Requirements
Must have
• logo
Should not have
• any colors outside of the logo

```html
<!DOCTYPE html>
<html lang="en">
<head>
<meta charset="utf-8">
<title>Vela Healthcare Postcard</title>
<link href="https://fonts.googleapis.com/css2?family=Montserrat:wght@500;600;700;800&family=Open+Sans:wght@400;600&display=swap" rel="stylesheet">
<style>
  :root{
    --blue:#1b7fc6;
    --blue-dark:#0f5796;
    --blue-light:#e4f1fb;
    --orange:#f26a21;
    --orange-dark:#d9531a;
    --ink:#1f3f66;
    --grey:#d7dbe0;
    --page:#eef0f2;
    --white:#ffffff;
  }
  *{box-sizing:border-box;margin:0;padding:0}
  html,body{width:900px;height:1200px;overflow:hidden;background:var(--page)}
  body{position:relative;font-family:"Open Sans",Arial,sans-serif;color:var(--ink)}
  .card{position:absolute;left:30px;width:840px;height:570px;background:var(--white);overflow:hidden;box-shadow:0 3px 12px rgba(0,0,0,.18)}
  .card--front{top:20px}
  .card--back{top:610px}
  .abs{position:absolute}
  .heading{font-family:"Montserrat",Arial,sans-serif}

  /* front */
  .exp-box{left:0;top:28px;width:380px;height:104px;background:var(--blue);color:var(--white);padding:14px 0 0 26px;clip-path:polygon(0 0,100% 0,88% 100%,0 100%)}
  .exp-box .small{font-size:27px;font-weight:700;letter-spacing:.5px}
  .exp-box .big{font-size:46px;font-weight:800;line-height:1.05}
  .exp-accent{left:0;top:132px;width:330px;height:8px;background:var(--orange)}
  .hero-photo{left:380px;top:0;width:460px;height:260px;background:linear-gradient(135deg,#f4f7fa 0%,#e3e9ef 45%,#e46a6a 70%,#f0e2da 100%)}
  .services-list{left:40px;top:160px;list-style:none;font-size:21px;font-weight:600;color:var(--ink);line-height:1.4}
  .services-list li::before{content:"";display:inline-block;width:9px;height:9px;background:var(--blue);margin-right:12px;vertical-align:middle}
  .beyond-band{left:0;top:248px;width:560px;height:74px;background:var(--orange);color:var(--white);padding:12px 0 0 30px;clip-path:polygon(0 0,100% 0,94% 100%,0 100%)}
  .beyond-band .line1{font-size:27px;font-weight:800;letter-spacing:.3px}
  .beyond-band .line2{font-size:15px;font-weight:600;letter-spacing:1px}
  .call{left:40px;top:344px;font-size:38px;font-weight:700;color:var(--blue-dark)}
  .book-btn{display:flex;align-items:center;justify-content:center;background:var(--orange);color:var(--white);font-family:"Montserrat",Arial,sans-serif;font-weight:800;border-radius:8px;border:3px solid var(--white);box-shadow:0 0 0 2px var(--orange-dark)}
  .book-btn--front{left:44px;top:416px;width:300px;height:58px;font-size:27px}
  .brand{display:flex;align-items:center;gap:8px;font-family:"Montserrat",Arial,sans-serif;font-weight:700;color:var(--blue);white-space:nowrap}
  .brand .dot{width:14px;height:14px;border-radius:50%;background:var(--orange);flex:none}
  .brand--front{left:415px;top:420px;font-size:19px}
  .couple-photo{left:625px;top:330px;width:215px;height:192px;background:linear-gradient(160deg,#dfeaf3 0%,#c9d8e6 40%,#e9d2c1 100%)}
  .footer{left:0;bottom:0;width:840px;height:50px;background:var(--blue);color:var(--white);font-size:24px;font-weight:600;padding:9px 0 0 36px}
  .footer-accent{left:0;bottom:50px;width:840px;height:5px;background:var(--orange)}

  /* back */
  .about-panel{left:0;top:0;width:480px;height:525px;background:var(--blue)}
  .about-title{left:30px;top:24px;color:var(--white);font-size:27px;font-weight:800}
  .about-text{left:30px;top:66px;width:420px;color:var(--white);font-size:13.5px;line-height:1.55}
  .book-btn--back{left:30px;top:268px;width:290px;height:52px;font-size:24px}
  .map{left:30px;top:345px;width:150px;height:150px;background:linear-gradient(135deg,#eef1e8 0%,#dfe6d6 50%,#cfdbe6 100%);border:3px solid var(--white)}
  .addresses{left:190px;top:385px;list-style:none;color:var(--white);font-size:11.5px;line-height:1.35}
  .addresses li{display:flex;align-items:flex-start;gap:6px;margin-bottom:12px;width:148px}
  .addresses svg{flex:none;margin-top:2px}
  .doctor-photo{left:350px;top:320px;width:130px;height:205px;background:linear-gradient(180deg,#f1f4f7 0%,#dbe5ee 60%,#8fb3d4 100%)}
  .back-footer{left:0;bottom:0;width:840px;height:45px;background:var(--blue-dark);color:var(--white);font-size:22px;font-weight:600;text-align:center;padding-top:8px;letter-spacing:.5px}
  .edge-curve{left:480px;top:0;width:40px;height:525px}
  .brand--back{left:555px;top:66px;font-size:18px}
  .stamp{left:750px;top:28px;width:66px;height:80px;background:var(--grey)}
  .address-lines{left:590px;top:260px;width:220px}
  .address-lines span{display:block;height:1px;background:var(--grey);margin-bottom:40px}
</style>
</head>
<body>

<section class="card card--front">
  <div class="abs hero-photo" role="img" aria-label="Cupped hands holding a red heart"></div>
  <div class="abs exp-box heading">
    <div class="small">OVER 35 YEARS OF</div>
    <div class="big">EXPERIENCE</div>
  </div>
  <div class="abs exp-accent"></div>
  <ul class="abs services-list">
    <li>Primary care &amp; Psychiatry</li>
    <li>Physical rehabilitation</li>
  </ul>
  <div class="abs beyond-band heading">
    <div class="line1">SERVICES THAT EXTEND</div>
    <div class="line2">BEYOND TRADITIONAL MEDICINE</div>
  </div>
  <div class="abs call heading">Call at - 123.456.789</div>
  <div class="abs book-btn book-btn--front">BOOK ONLINE NOW</div>
  <div class="abs couple-photo" role="img" aria-label="Smiling senior couple"></div>
  <div class="abs brand brand--front"><span class="dot"></span>Vela Healthcare</div>
  <div class="abs footer-accent"></div>
  <div class="abs footer heading">Our website - www.yourwebsite.com</div>
</section>

<section class="card card--back">
  <div class="abs about-panel"></div>
  <svg class="abs edge-curve" viewBox="0 0 40 525" preserveAspectRatio="none" aria-hidden="true">
    <path d="M0 0 Q40 262 0 525 Z" fill="var(--orange)"/>
  </svg>
  <h2 class="abs about-title heading">ABOUT OUR COMPANY</h2>
  <p class="abs about-text">Vela Healthcare is based in Springfield and has over 35 years of experience. With many offices across the region, our goal is simple: to help our community. We care for patients of every age, from infancy to later years. Our group grew from a single practice into a trusted network of physicians and therapists, and our team remains devoted to giving back to the families who count on us every day.</p>
  <div class="abs book-btn book-btn--back">BOOK ONLINE NOW</div>
  <div class="abs map" role="img" aria-label="Street map showing clinic locations"></div>
  <ul class="abs addresses">
    <li><svg width="10" height="14" viewBox="0 0 10 14" aria-hidden="true"><path d="M5 0a5 5 0 0 0-5 5c0 4 5 9 5 9s5-5 5-9a5 5 0 0 0-5-5z" fill="var(--orange)"/><circle cx="5" cy="5" r="2" fill="var(--white)"/></svg><span>1200 Maple Grove Ave, Springfield, IL 60100</span></li>
    <li><svg width="10" height="14" viewBox="0 0 10 14" aria-hidden="true"><path d="M5 0a5 5 0 0 0-5 5c0 4 5 9 5 9s5-5 5-9a5 5 0 0 0-5-5z" fill="var(--orange)"/><circle cx="5" cy="5" r="2" fill="var(--white)"/></svg><span>3400 Harbor Lane, Springfield, IL 60120</span></li>
  </ul>
  <div class="abs doctor-photo" role="img" aria-label="Physician in white coat"></div>
  <div class="abs brand brand--back"><span class="dot"></span>Vela Healthcare</div>
  <div class="abs stamp"></div>
  <div class="abs back-footer heading">www.yourwebsite.com</div>
</section>

</body>
</html>
```